Super Greens Label for Supplement Bottle

We want to design a front label for a health supplement bottle. The product is called Meadow Twist Chews™. This will be a new product so there is no current website for the product. The focus is on supergreens that taste great and deliver support for energy, digestion, and immune defense.
We want it to be modern, vibrant and appealing.
Bottle size: standard size supplement CLEAR bottle size, with white child resistant cap and the label panel dimensions are 3” x 7”. The label should be primarily white and green, with a touch of red; (see color palettes)/it can also ONLY be white and green. See samples attached.
We are only focused on the front of the bottle design, not on the back, but leave space for the supplement panel and other text on the back.
So the text for the front of the bottle is:
RT Balden's
Meadow Twist Chews™
Super Greens Blend for:
Energy, Digestion, and Immune Support*
60 Gummies | Dietary Supplement
Raspberry Flavor Gummies
Off to side of the label:
Non-GMO
Vegan Friendly
Plant-Based
Gelatin Free
Colors
Designer to choose colors to be used in the design.

```html
<!DOCTYPE html>
<html lang="en">
<head>
<meta charset="utf-8">
<title>RT Balden's Meadow Twist Chews – Front Label</title>
<link href="https://fonts.googleapis.com/css2?family=Anton&display=swap" rel="stylesheet">
<style>
  :root {
    --page-bg: #f4f4f4;
    --label-white: #ffffff;
    --green-deep: #127a52;
    --green-mid: #1f9470;
    --green-light: #5cbfa0;
    --green-pale: #8fd8bf;
    --green-ink: #1e8a62;
  }
  * { margin: 0; padding: 0; box-sizing: border-box; }
  html, body {
    width: 1200px; height: 960px; overflow: hidden;
    background: var(--page-bg);
    font-family: "Anton", "Impact", sans-serif;
  }
  .label {
    position: absolute; left: 270px; top: 45px;
    width: 660px; height: 870px;
    background: var(--label-white);
    overflow: hidden;
  }
  .hero-band {
    position: absolute; left: 0; top: 0; width: 660px; height: 696px;
    background:
      radial-gradient(ellipse 260px 200px at 30% 50%, rgba(92,191,160,.55), transparent 70%),
      radial-gradient(ellipse 180px 300px at 95% 55%, rgba(143,216,191,.6), transparent 70%),
      radial-gradient(ellipse 200px 160px at 60% 30%, rgba(18,122,82,.8), transparent 70%),
      linear-gradient(90deg, var(--green-pale) 0%, var(--green-mid) 12%, var(--green-deep) 45%, var(--green-mid) 75%, var(--green-light) 100%);
  }
  .brand-tag {
    position: absolute; left: 52px; top: 84px; width: 366px; height: 76px;
    background: var(--label-white); border-radius: 4px;
    color: var(--green-ink); font-size: 52px; line-height: 76px;
    text-align: center; letter-spacing: 1px; text-transform: uppercase;
  }
  .product-name {
    position: absolute; left: 50px; top: 178px;
    color: var(--label-white); text-transform: uppercase; font-weight: 400;
    font-size: 112px; line-height: 132px; letter-spacing: 2px;
  }
  .product-name span { display: block; }
  .product-name sup { font-size: 26px; vertical-align: top; line-height: 1; position: relative; top: 14px; }
  .claims-rail {
    position: absolute; left: 524px; top: 0; width: 96px; height: 432px;
    background: var(--label-white); border-radius: 0 0 10px 10px;
    display: flex; flex-direction: column; align-items: center;
    justify-content: space-around; padding: 18px 0;
  }
  .claims-rail svg { width: 74px; height: 74px; }
  .claims-rail text {
    font-family: "Anton", "Impact", sans-serif;
    fill: var(--green-ink); text-anchor: middle; text-transform: uppercase;
  }
  .benefit-line {
    position: absolute; left: 52px; top: 608px; width: 580px;
    color: var(--label-white); font-size: 26px; line-height: 30px;
    text-transform: uppercase; letter-spacing: .3px;
  }
  .benefit-line sup { font-size: 14px; }
  .count {
    position: absolute; left: 50px; top: 712px;
    color: var(--green-ink); font-size: 100px; line-height: 120px;
  }
  .flavor-pill {
    position: absolute; left: 179px; top: 731px; width: 434px; height: 35px;
    background: var(--green-ink); border-radius: 4px;
    color: var(--label-white); font-size: 26px; line-height: 35px;
    padding-left: 10px; text-transform: uppercase;
  }
  .supplement-note {
    position: absolute; left: 189px; top: 772px;
    color: var(--green-ink); font-size: 26px; line-height: 36px;
    text-transform: uppercase;
  }
</style>
</head>
<body>
  <main class="label">
    <section class="hero-band">
      <div class="brand-tag">RT Balden's</div>
      <h1 class="product-name">
        <span>Meadow</span>
        <span>Twist</span>
        <span>Chews<sup>™</sup></span>
      </h1>
      <aside class="claims-rail" aria-label="Non-GMO, Vegan Friendly, Plant-Based, Gelatin Free">
        <svg viewBox="0 0 74 74" role="img" aria-label="Non-GMO">
          <circle cx="37" cy="37" r="33" fill="none" stroke="#1e8a62" stroke-width="2.5"/>
          <text x="37" y="35" font-size="15">NON</text>
          <text x="37" y="52" font-size="15">GMO</text>
        </svg>
        <svg viewBox="0 0 74 74" role="img" aria-label="Vegan friendly">
          <circle cx="37" cy="37" r="33" fill="none" stroke="#1e8a62" stroke-width="2.5"/>
          <text x="37" y="35" font-size="14">VEGAN</text>
          <text x="37" y="51" font-size="11">FRIENDLY</text>
        </svg>
        <svg viewBox="0 0 74 74" role="img" aria-label="Plant-based">
          <circle cx="37" cy="37" r="33" fill="none" stroke="#1e8a62" stroke-width="2.5"/>
          <text x="37" y="35" font-size="14">PLANT</text>
          <text x="37" y="51" font-size="14">BASED</text>
        </svg>
        <svg viewBox="0 0 74 74" role="img" aria-label="Gelatin free">
          <circle cx="37" cy="37" r="33" fill="none" stroke="#1e8a62" stroke-width="2.5"/>
          <text x="37" y="35" font-size="12">GELATIN</text>
          <text x="37" y="51" font-size="14">FREE</text>
        </svg>
      </aside>
      <p class="benefit-line">Super Greens Blend for Energy, Digestion,<br>and Immune Support<sup>*</sup></p>
    </section>
    <div class="count">60</div>
    <div class="flavor-pill">Raspberry Flavor Gummies</div>
    <div class="supplement-note">Dietary Supplement</div>
  </main>
</body>
</html>
```